Book Cover For An Investment Book On Trend Trading

We are in need of a clean modern book cover with a modern feel for a new book on trend trading.

Task Description
I need a book cover for traditional print and eReaders (Lumora, etc.) for a new financial investment book targeted at people who want to manage their own money. The title is “A Quick Primer for Portfolio Growth” with subtitle “Riding Upswings and Dodging Slumps Wisely” written by, Gordon Pike.

In brief, simple techniques to identify the direction of the market and then actionable steps to trade with the trend for financial success are shown. No more endless roller coaster ride watching your investments rise and then precipitously fall.

There is discussion about famous historic and recent bubbles and human nature. The poor performance of a number of hedge funds is reviewed and suggest the smartest person in the room may be you managing you own money.

This is a practical, hands-on guide targeted at the novice to intermediate experienced investor.

Note: We have a temp logo attached. If you want to create a new one, feel free.

www.steadyslopemarkets.com

Please include in the design a picture of the author an description. Use place holder for now.

Please also include 3 testimonials.
Updates

The dimensions are 8.5 x 5.5 x .75

Industry/Entity Type

Financial

Requirements
Nice to have
• Three testimonials

Author Pic (use place holder)
and back ground

A Graphic of trend lines on A recent Birchfield Stock Chart or VORNA. (Go to finderly and type in Birchfield Stock and trend lines.)

```html
<!DOCTYPE html>
<html lang="en">
<head>
<meta charset="utf-8">
<title>A Quick Primer for Portfolio Growth – Book Cover</title>
<link rel="stylesheet" href="https://fonts.googleapis.com/css2?family=Anton&family=Russo+One&family=Open+Sans:wght@400;700;800&display=swap">
<style>
  :root {
    --bg: #4a4a4a;
    --navy-deep: #1c1550;
    --navy: #27297a;
    --royal: #2c4fb8;
    --sky: #1aa3e8;
    --sky-light: #34b8f0;
    --lavender: #8f8fd0;
    --lavender-dark: #6d6db8;
    --chart-dark: #1f3f8f;
    --chart-light: #8fb6e8;
    --white: #ffffff;
    --ink: #120f3c;
  }
  * { margin: 0; padding: 0; box-sizing: border-box; }
  html, body { width: 1200px; height: 999px; overflow: hidden; }
  body { background: var(--bg); font-family: "Open Sans", sans-serif; }

  .cover-wrap {
    position: absolute; left: 60px; top: 110px;
    width: 1080px; height: 780px;
    display: flex;
  }

  /* Back cover */
  .back-cover {
    width: 500px; height: 100%;
    background: linear-gradient(180deg, var(--navy-deep) 0%, var(--navy) 35%, var(--royal) 62%, var(--sky) 100%);
    color: var(--white);
    padding: 38px 40px 30px 40px;
    position: relative;
  }
  .back-heading {
    font-weight: 700; font-size: 23px; margin-bottom: 10px;
  }
  .back-text {
    font-size: 12.5px; line-height: 1.42; text-align: justify; margin-bottom: 16px;
  }
  .author-section {
    position: absolute; left: 40px; right: 40px; top: 470px;
    display: flex; gap: 18px;
  }
  .author-bio { flex: 1; }
  .author-photo-placeholder {
    width: 132px; height: 170px; background: var(--white);
    border-radius: 16px; flex-shrink: 0; margin-top: 0;
  }
  .back-url {
    position: absolute; right: 42px; bottom: 28px;
    font-size: 12.5px;
  }

  /* Spine */
  .spine {
    width: 70px; height: 100%;
    background: linear-gradient(90deg, var(--royal) 0%, var(--sky-light) 45%, var(--royal) 100%);
    display: flex; align-items: center; justify-content: center;
    border-left: 1px solid var(--navy-deep);
    border-right: 1px solid var(--navy-deep);
  }
  .spine-title {
    writing-mode: vertical-rl;
    font-family: "Anton", sans-serif; font-size: 34px; color: var(--white);
    letter-spacing: 0.5px; white-space: nowrap;
  }

  /* Front cover */
  .front-cover {
    width: 510px; height: 100%;
    display: flex; flex-direction: column;
    background: var(--navy);
  }
  .title-block {
    height: 250px;
    background: linear-gradient(180deg, var(--sky) 0%, var(--royal) 30%, var(--navy) 100%);
    color: var(--white); text-align: center;
    padding-top: 18px;
    border-bottom: 6px solid #3a3a6a;
  }
  .title-line-1 {
    font-family: "Anton", sans-serif; font-size: 74px; line-height: 1; letter-spacing: 1px;
  }
  .title-line-2 {
    font-family: "Russo One", sans-serif; font-size: 37px; line-height: 1.1; margin-top: 4px;
  }
  .title-line-3 {
    font-family: "Anton", sans-serif; font-size: 82px; line-height: 1; margin-top: 2px;
  }
  .chart-visual {
    height: 320px;
    background: linear-gradient(135deg, var(--chart-dark) 0%, #3b64b8 45%, var(--chart-light) 75%, #4a6fc0 100%);
  }
  .subtitle-band {
    height: 140px;
    background: linear-gradient(180deg, var(--sky-light) 0%, var(--sky) 25%, var(--royal) 100%);
    display: flex; align-items: center; justify-content: center;
    border-top: 8px solid var(--sky);
  }
  .subtitle {
    font-weight: 700; font-size: 30px; line-height: 1.2; color: var(--white); text-align: center;
  }
  .author-band {
    height: 40px; background: var(--lavender);
    display: flex; align-items: center; justify-content: center;
  }
  .author-name {
    font-weight: 800; font-size: 24px; color: var(--ink);
  }
  .bottom-strip { flex: 1; background: var(--lavender-dark); }
</style>
</head>
<body>
  <div class="cover-wrap">
    <section class="back-cover">
      <h2 class="back-heading">Testimonials</h2>
      <p class="back-text">Lorem ipsum dolor sit amet, consectetur adipiscing elit. Curabitur lacinia congue varius. Nunc ut augue cursus lectus aliquet elementum. Suspendisse semper sodales eros id cursus. Nunc lacinia adipiscing nibh. Maecenas eu dui velit. Sed nec sem leo. In a lacus scelerisque, condimentum turpis a, mollis orci. Integer nec orci justo. Nulla non dolor neque. Etiam condimentum erat sem, et posuere orci aliquam pellentesque. In nec ante quis urna gravida interdum. In lobortis elementum neque, nec interdum purus blandit sed. Curabitur adipiscing suscipit nunc ac molestie.</p>
      <p class="back-text">Lorem ipsum dolor sit amet, consectetur adipiscing elit. Curabitur lacinia congue varius. Nunc ut augue cursus lectus aliquet elementum. Suspendisse semper sodales eros id cursus. Nunc lacinia adipiscing nibh. Maecenas eu dui velit. Sed nec sem leo. In a lacus scelerisque, condimentum turpis a, mollis orci. Integer nec orci justo. Nulla non dolor neque. Etiam condimentum erat sem, et posuere orci aliquam pellentesque. In nec ante quis urna gravida interdum. In lobortis elementum neque, nec interdum purus blandit sed. Curabitur adipiscing suscipit nunc ac molestie.</p>

      <div class="author-section">
        <div class="author-bio">
          <h2 class="back-heading">Author</h2>
          <p class="back-text">Lorem ipsum dolor sit amet, consectetur adipiscing elit. Curabitur lacinia congue varius. Nunc ut augue cursus lectus aliquet elementum. Suspendisse semper sodales eros id cursus. Nunc lacinia adipiscing nibh. Maecenas eu dui velit. Sed nec sem leo. In a lacus scelerisque, condimentum turpis a, mollis orci. Integer nec orci justo. Nulla non dolor neque. Etiam condimentum erat sem, et neque.</p>
        </div>
        <div class="author-photo-placeholder" role="img" aria-label="Author photo placeholder"></div>
      </div>

      <p class="back-url">www.steadyslopemarkets.com</p>
    </section>

    <section class="spine">
      <h2 class="spine-title">A Quick Primer for Portfolio Growth</h2>
    </section>

    <section class="front-cover">
      <header class="title-block">
        <h1>
          <span class="title-line-1" style="display:block">A QUICK PRIMER</span>
          <span class="title-line-2" style="display:block">FOR PORTFOLIO</span>
          <span class="title-line-3" style="display:block">GROWTH</span>
        </h1>
      </header>
      <div class="chart-visual" role="img" aria-label="Blue stock market chart illustration with price figures, candlesticks and a rising trend line"></div>
      <div class="subtitle-band">
        <p class="subtitle">Riding Upswings and<br>Dodging Slumps Wisely</p>
      </div>
      <div class="author-band">
        <p class="author-name">Gordon Pike</p>
      </div>
      <div class="bottom-strip"></div>
    </section>
  </div>
</body>
</html>
```